Double sided 8.5x11 Flyer

The attached text should be in the flyer. this is an election flyer for a board of director role for automotive racing industry. Try to make it exciting!

```html
<!DOCTYPE html>
<html lang="en">
<head>
<meta charset="utf-8">
<title>Dana Whitcomb – Board of Directors Flyer</title>
<link href="https://fonts.googleapis.com/css2?family=Montserrat:wght@500;700;800;900&family=Open+Sans:wght@400;600;700&display=swap" rel="stylesheet">
<style>
  :root{
    --forest:#0f3a35;
    --forest-deep:#0a2b27;
    --emerald:#1d7a52;
    --emerald-light:#2e9a69;
    --signal-red:#d3222a;
    --ink:#262a2c;
    --muted:#5c6466;
    --paper:#ffffff;
    --rule:#d9dedd;
    --stage:#f1f2f1;
    --photo-a:#5d6b66;
    --photo-b:#b9b2a2;
  }
  *{box-sizing:border-box;margin:0;padding:0}
  html,body{width:784px;height:1200px;overflow:hidden}
  body{background:var(--stage);font-family:"Open Sans",Arial,sans-serif;color:var(--ink);
    display:flex;flex-direction:column;align-items:center;justify-content:center;gap:16px}
  .sheet{width:452px;height:585px;background:var(--paper);position:relative;overflow:hidden;
    box-shadow:0 2px 8px rgba(0,0,0,.15)}
  h1,h2,h3,.name{font-family:"Montserrat",Arial,sans-serif}

  /* ---------- front ---------- */
  .front{display:grid;grid-template-columns:176px 1fr;grid-template-rows:1fr 34px}
  .pitch{background:var(--forest);color:var(--paper);padding:16px 14px 0;display:flex;flex-direction:column;gap:8px}
  .pitch-head{display:flex;gap:8px;align-items:flex-start}
  .stop-sign{flex:0 0 34px}
  .pitch h1{font-size:11.5px;font-weight:800;line-height:1.25}
  .pitch p{font-size:6.6px;line-height:1.5;color:#dfe9e6}
  .pitch p strong{color:var(--paper)}
  .pitch-photo{margin:4px -14px 0;flex:1;background:linear-gradient(135deg,var(--photo-b),var(--photo-a))}
  .profile{display:flex;flex-direction:column}
  .portrait{height:136px;background:linear-gradient(160deg,#e7e9e8,#9aa3a1)}
  .name-band{background:var(--forest-deep);color:var(--paper);padding:7px 14px;text-align:center}
  .name{font-size:15px;font-weight:900;letter-spacing:1px}
  .role{font-size:6.5px;letter-spacing:.5px;color:#b9d7cb;text-transform:uppercase}
  .topics{padding:8px 12px 4px;display:flex;flex-direction:column;gap:7px}
  .topic h3{display:flex;align-items:center;gap:5px;font-size:7px;font-weight:800;color:var(--paper);
    background:var(--emerald);padding:3px 6px;text-transform:uppercase}
  .topic p{font-size:6.4px;line-height:1.5;color:var(--muted);padding-top:3px}
  .passions h2{background:var(--forest);color:var(--paper);font-size:7.5px;font-weight:800;padding:5px 12px;
    display:flex;gap:6px;align-items:center;text-transform:uppercase}
  .passion-list{list-style:none;padding:6px 12px;display:grid;gap:3px}
  .passion-list li{font-size:6.6px;display:flex;gap:5px;align-items:center}
  .contact-bar{grid-column:1 / 3;display:grid;grid-template-columns:1fr 150px}
  .contact-bar .slogan{background:var(--forest-deep);color:var(--paper);font-family:"Montserrat",sans-serif;
    font-weight:700;font-size:8px;display:flex;align-items:center;padding-left:14px;text-transform:uppercase}
  .contact-bar .phone{background:var(--emerald);color:var(--paper);font-family:"Montserrat",sans-serif;
    font-weight:800;font-size:11px;display:flex;align-items:center;justify-content:center;gap:6px}

  /* ---------- back ---------- */
  .back{display:flex;flex-direction:column}
  .band{background:var(--forest);color:var(--paper);text-align:center;font-size:11px;font-weight:900;
    padding:9px 0;letter-spacing:.5px;text-transform:uppercase}
  .band.slim{font-size:9px;padding:6px 0}
  .roles{display:grid;grid-template-columns:1fr 1fr;gap:10px 16px;padding:12px 16px}
  .role-item h3{font-size:7.3px;font-weight:800;color:var(--emerald);border-left:3px solid var(--signal-red);padding-left:5px}
  .role-item p{font-size:6.4px;line-height:1.5;color:var(--muted);padding-top:2px}
  .shop-photo{height:112px;margin:0 16px 10px;background:linear-gradient(120deg,#c6c9c3,var(--photo-a) 60%,#8a6d55)}
  .endorsements{display:grid;grid-template-columns:1fr 1fr;gap:10px;padding:8px 16px 10px}
  table{border-collapse:collapse;width:100%;font-size:6.2px}
  th{background:var(--emerald);color:var(--paper);text-align:left;padding:3px 4px;font-family:"Montserrat",sans-serif}
  td{padding:3.5px 4px;border-bottom:1px solid var(--rule)}
  tr:nth-child(even) td{background:#f1f5f3}
  .call-bar{margin-top:auto;background:var(--emerald);color:var(--paper);display:flex;justify-content:space-between;
    align-items:center;padding:0 16px;height:34px}
  .call-bar .call{font-family:"Montserrat",sans-serif;font-weight:800;font-size:11px}
  .call-bar .web{font-size:6.5px;text-align:right;line-height:1.4}
  .call-bar .web strong{font-size:8px}
</style>
</head>
<body>

<!-- Front side -->
<section class="sheet front">
  <div class="pitch">
    <div class="pitch-head">
      <svg class="stop-sign" viewBox="0 0 34 34" aria-hidden="true">
        <polygon points="10,1 24,1 33,10 33,24 24,33 10,33 1,24 1,10" fill="var(--signal-red)" stroke="#fff" stroke-width="1.5"/>
        <text x="17" y="20.5" text-anchor="middle" font-family="Montserrat,sans-serif" font-weight="900" font-size="9" fill="#fff">STOP</text>
      </svg>
      <h1>I need 10 seconds of your time. I promise it's important. Read below...</h1>
    </div>
    <p><strong>As a board candidate</strong> I bring two decades of hands-on racing experience, from the pit lane to the parts counter, and a clear plan for our growth.</p>
    <p>I believe every member deserves a voice. Our industry is changing fast, and we need leaders who listen and act.</p>
    <p>Together we can open new markets, protect our right to race, and bring young talent into the sport we love.</p>
    <p><strong>Cast your vote for steady, proven leadership this season.</strong></p>
    <div class="pitch-photo" role="img" aria-label="Photo of a performance parts warehouse with stacked inventory"></div>
  </div>

  <div class="profile">
    <div class="portrait" role="img" aria-label="Portrait photo of the candidate in a suit"></div>
    <div class="name-band">
      <div class="name">DANA WHITCOMB</div>
      <div class="role">Candidate for Board of Directors</div>
    </div>
    <div class="topics">
      <div class="topic">
        <h3><svg width="7" height="7" viewBox="0 0 10 10" aria-hidden="true"><circle cx="5" cy="3" r="2.4" fill="#fff"/><path d="M0.5 10a4.5 4 0 0 1 9 0z" fill="#fff"/></svg>About Me</h3>
        <p>Racing team owner, parts distributor and lifelong enthusiast with over twenty years serving the motorsport community.</p>
      </div>
      <div class="topic">
        <h3><svg width="7" height="7" viewBox="0 0 10 10" aria-hidden="true"><rect x="1" y="3" width="8" height="6" fill="#fff"/><rect x="3.5" y="1" width="3" height="2.5" fill="none" stroke="#fff"/></svg>My Experience</h3>
        <p>Led regional sales for a major performance brand, built dealer networks and sat on three advisory panels for racing events.</p>
      </div>
      <div class="topic">
        <h3><svg width="7" height="7" viewBox="0 0 10 10" aria-hidden="true"><circle cx="5" cy="5" r="4" fill="none" stroke="#fff" stroke-width="1.4"/><circle cx="5" cy="5" r="1.6" fill="#fff"/></svg>My Goals for the Board</h3>
        <p>Grow membership, expand trade show reach, support small shops and defend motorsport on public roads and tracks nationwide.</p>
      </div>
    </div>
    <div class="passions">
      <h2><svg width="8" height="8" viewBox="0 0 10 10" aria-hidden="true"><path d="M5 9 1 5a2.3 2.3 0 0 1 4-3 2.3 2.3 0 0 1 4 3z" fill="var(--signal-red)"/></svg>My Passions Keep Me Motivated</h2>
      <ul class="passion-list">
        <li><svg width="7" height="7" viewBox="0 0 10 10" aria-hidden="true"><path d="M1 5.5 4 8.5 9 1.5" fill="none" stroke="var(--emerald)" stroke-width="2"/></svg>Weekend drag racing with my own team</li>
        <li><svg width="7" height="7" viewBox="0 0 10 10" aria-hidden="true"><path d="M1 5.5 4 8.5 9 1.5" fill="none" stroke="var(--emerald)" stroke-width="2"/></svg>Building classic muscle cars</li>
        <li><svg width="7" height="7" viewBox="0 0 10 10" aria-hidden="true"><path d="M1 5.5 4 8.5 9 1.5" fill="none" stroke="var(--emerald)" stroke-width="2"/></svg>Mentoring young technicians</li>
        <li><svg width="7" height="7" viewBox="0 0 10 10" aria-hidden="true"><path d="M1 5.5 4 8.5 9 1.5" fill="none" stroke="var(--emerald)" stroke-width="2"/></svg>Helping small shops grow</li>
        <li><svg width="7" height="7" viewBox="0 0 10 10" aria-hidden="true"><path d="M1 5.5 4 8.5 9 1.5" fill="none" stroke="var(--emerald)" stroke-width="2"/></svg>Supporting track safety</li>
        <li><svg width="7" height="7" viewBox="0 0 10 10" aria-hidden="true"><path d="M1 5.5 4 8.5 9 1.5" fill="none" stroke="var(--emerald)" stroke-width="2"/></svg>Family time at the track</li>
      </ul>
    </div>
  </div>

  <div class="contact-bar">
    <div class="slogan">Vote Dana Whitcomb for the Board</div>
    <div class="phone">
      <svg width="10" height="10" viewBox="0 0 10 10" aria-hidden="true"><path d="M2 0.8 3.6 2.6 2.8 3.8C3.5 5.2 4.8 6.5 6.2 7.2L7.4 6.4 9.2 8 8.2 9.4C4.5 9.2 0.8 5.5 0.6 1.8z" fill="#fff"/></svg>
      (555) 014-2287
    </div>
  </div>
</section>

<!-- Back side -->
<section class="sheet back">
  <h2 class="band">The Industry I've Played a Key Role In</h2>
  <div class="roles">
    <div class="role-item"><h3>Performance Parts Distribution</h3><p>Supplied over four hundred shops with engine, suspension and braking parts across the region.</p></div>
    <div class="role-item"><h3>Race Team Ownership</h3><p>Fielded a winning drag team for twelve seasons with multiple regional titles.</p></div>
    <div class="role-item"><h3>Dealer Network Growth</h3><p>Built a network of thirty dealers and trained staff on modern performance products.</p></div>
    <div class="role-item"><h3>Trade Show Leadership</h3><p>Organized exhibitor halls and helped draw record crowds to annual industry expos.</p></div>
    <div class="role-item"><h3>Youth Technical Programs</h3><p>Launched scholarships that bring students into automotive service and race engineering careers.</p></div>
    <div class="role-item"><h3>Track Safety Advocacy</h3><p>Worked with promoters to upgrade barriers, fire crews and driver safety rules.</p></div>
  </div>
  <div class="shop-photo" role="img" aria-label="Photo of a busy automotive workshop with cars on lifts"></div>
  <h2 class="band slim">Endorsements From Industry</h2>
  <div class="endorsements">
    <table>
      <tr><th>Name</th><th>Endorsement</th></tr>
      <tr><td>Rick Alvarez</td><td>Proven leader for our sport</td></tr>
      <tr><td>Janet Moore</td><td>Always puts members first</td></tr>
      <tr><td>Tom Kessler</td><td>Knows racing inside out</td></tr>
      <tr><td>Lena Ortiz</td><td>A true champion for shops</td></tr>
    </table>
    <table>
      <tr><th>Name</th><th>Endorsement</th></tr>
      <tr><td>Paul Brandt</td><td>Honest, driven and fair</td></tr>
      <tr><td>Carla Nguyen</td><td>Builds strong industry ties</td></tr>
      <tr><td>Mike Dorsey</td><td>The right voice now</td></tr>
      <tr><td>Sara Quinlan</td><td>Gets real results fast</td></tr>
    </table>
  </div>
  <div class="call-bar">
    <div class="call">CALL US NOW (555) 014-2287</div>
    <div class="web">Visit us for more details<br><strong>www.Whitcomb4Board.com</strong></div>
  </div>
</section>

</body>
</html>
```